Nutrition product information web site

Nutrition Website (see upload) without Shop function but link to Brixel ASIN number that customer could order from Brixel direct. Content must be easily editable without coding. Web environment must be responsive to support mobile devices as well. design should be modern and clear. loading of web elements must be fast. not too much time consuming features.

Industry/Entity Type

Nutrition

Number of Pages Required

5+ page

Font styles to use
Sans Serif

Colors
33b8a4
9bcb3c
0255a3
0a90cc
a54499

Requirements
Must have
• read attached document
Nice to have
• read attached document
Should not have
• read attached document

```html
<!DOCTYPE html>
<html lang="en">
<head>
<meta charset="utf-8">
<title>Veluna – Nutrition</title>
<link href="https://fonts.googleapis.com/css2?family=Poppins:wght@300;400;600&family=Open+Sans:wght@400;600&family=PT+Sans:wght@400&display=swap" rel="stylesheet">
<style>
  :root{
    --purple:#a3449a;
    --blue:#0255a3;
    --ink:#222222;
    --text:#3a3a3a;
    --grey-bg:#eeeeee;
    --meta-bg:#f0f0f0;
    --footer-nav:#e9e9e9;
    --rule:#d6d6d6;
    --white:#ffffff;
  }
  *{box-sizing:border-box;margin:0;padding:0}
  html,body{width:1200px;height:2439px;overflow:hidden}
  body{background:var(--white);font-family:"Open Sans",sans-serif;color:var(--text);position:relative}

  /* top bar */
  .topbar{position:absolute;left:0;top:0;width:1200px;height:36px;background:var(--purple)}
  .social{position:absolute;display:flex;gap:9px}
  .social span{width:22px;height:22px;border-radius:50%;background:rgba(0,0,0,.25);border:1px solid rgba(255,255,255,.5)}
  .topbar .social{left:868px;top:7px}
  .lang{position:absolute;left:980px;top:9px;display:flex;align-items:center;gap:6px;color:var(--white);font-size:12px}
  .lang i{width:22px;height:16px;border-radius:50%;background:#d9dde8;display:block}

  /* header */
  .header{position:absolute;left:0;top:36px;width:1200px;height:107px;background:var(--white)}
  .brand{position:absolute;left:114px;top:-22px;display:flex;flex-direction:column;align-items:center;width:150px}
  .brand .mark{width:66px;height:66px;border-radius:50%;border:3px solid var(--ink);background:var(--white)}
  .brand .name{font-family:"Poppins",sans-serif;font-weight:600;font-size:30px;letter-spacing:3px;color:var(--ink);margin-top:6px;line-height:1}
  .nav{position:absolute;top:44px;left:583px;display:flex;align-items:center;font-family:"Poppins",sans-serif;font-size:14px;color:var(--ink)}
  .nav a{color:inherit;text-decoration:none;padding:0 10px;position:relative}
  .nav .dot{width:5px;height:5px;border-radius:50%;background:#bbbbbb;margin:0 12px}
  .nav a.active::after{content:"";position:absolute;left:0;right:0;bottom:-10px;height:3px;background:var(--purple)}

  /* hero */
  .hero{position:absolute;left:0;top:143px;width:1200px;height:486px;
    background:linear-gradient(180deg,#8d7e6f 0%,#b9aa98 35%,#d7cbb9 60%,#a68a6a 66%,#c9ad88 100%)}
  .hero-products{position:absolute;left:553px;top:77px;width:520px;height:365px;border-radius:18px;
    background:linear-gradient(180deg,#f3f3f3 0%,#e3e6e9 70%,#cfd6dc 100%);opacity:.92}
  .hero-copy{position:absolute;left:114px;top:160px;color:var(--white)}
  .hero-copy h1{font-family:"Poppins",sans-serif;font-weight:300;font-size:32px;line-height:42px;letter-spacing:.5px}
  .hero-copy p{font-family:"Poppins",sans-serif;font-size:21px;margin-top:4px}
  .btn-hero{position:absolute;left:114px;top:283px;width:336px;height:54px;background:var(--blue);color:var(--white);
    font-family:"Poppins",sans-serif;font-size:20px;display:flex;align-items:center;justify-content:center;letter-spacing:.5px;text-decoration:none}

  /* section titles */
  .section-title{position:absolute;left:0;width:1200px;text-align:center;font-family:"Poppins",sans-serif;font-weight:400;font-size:35px;color:var(--ink)}
  .section-title b{color:var(--purple);font-weight:600}
  .divider{position:absolute;left:382px;width:436px;height:22px}
  .divider::before{content:"";position:absolute;left:0;right:0;top:10px;height:2px;background:var(--rule)}
  .divider::after{content:"";position:absolute;left:207px;top:0;width:22px;height:22px;border-radius:50%;border:2px solid #aaaaaa;background:var(--white)}
  .on-grey .divider::after{background:var(--grey-bg)}

  .btn{display:inline-flex;align-items:center;justify-content:center;background:var(--blue);color:var(--white);
    font-family:"Poppins",sans-serif;font-size:12.5px;text-decoration:none;height:25px;width:104px}

  /* about */
  .about{position:absolute;left:0;top:629px;width:1200px;height:443px}
  .about .section-title{top:64px}
  .about .divider{top:120px}
  .about h3{position:absolute;top:166px;left:0;width:1200px;text-align:center;font-size:16px;font-weight:600;color:var(--ink)}
  .about .lead{position:absolute;top:198px;left:170px;width:860px;text-align:center;font-size:12.5px;line-height:26px}
  .about .btn{position:absolute;left:545px;top:337px}

  /* products */
  .products{position:absolute;left:0;top:1072px;width:1200px;height:663px;background:var(--grey-bg)}
  .products .section-title{top:64px}
  .products .divider{top:120px}
  .product-grid{position:absolute;top:175px;left:148px;display:flex;gap:20px}
  .product-card{width:224px;height:413px;background:var(--white);padding:6px;text-align:center;box-shadow:0 1px 3px rgba(0,0,0,.06)}
  .product-image{height:210px;background:linear-gradient(180deg,#e8e8e8 0%,#dedede 100%)}
  .product-card h4{font-family:"Poppins",sans-serif;font-weight:400;font-size:17px;line-height:21px;color:var(--ink);margin-top:22px;height:46px;letter-spacing:.5px}
  .product-card p{font-family:"PT Sans",sans-serif;font-size:13px;line-height:17px;margin:10px 8px 0;color:var(--text)}
  .product-card .btn{margin-top:14px}

  /* blog */
  .blog{position:absolute;left:0;top:1735px;width:1200px;height:623px}
  .blog .section-title{top:60px}
  .blog .divider{top:119px}
  .blog-grid{position:absolute;top:187px;left:112px;display:flex;gap:37px}
  .post{width:301px;height:361px;border:1px solid #e4e4e4;background:var(--white);position:relative}
  .post-image{height:179px;position:relative}
  .post-image.beach{background:linear-gradient(180deg,#2f8fe0 0%,#7fc0f0 55%,#e6dccb 100%)}
  .post-image.waist{background:linear-gradient(180deg,#5f7f8c 0%,#a5b3b6 50%,#4a5b6e 100%)}
  .post-image.fitness{background:linear-gradient(180deg,#ffffff 0%,#f2eeee 60%,#e6c4c8 100%)}
  .date{position:absolute;left:0;bottom:0;background:var(--purple);color:var(--white);font-size:12px;padding:0 14px;height:36px;display:flex;align-items:center}
  .meta{height:37px;background:var(--meta-bg);display:flex;align-items:center;padding:0 14px;font-size:11.5px;color:#666666}
  .meta .author{display:flex;align-items:center;gap:8px;flex:1}
  .meta .stats{display:flex;gap:14px;align-items:center}
  .meta .stats span{display:flex;align-items:center;gap:6px}
  .meta svg{fill:#777777}
  .post h4{font-family:"Poppins",sans-serif;font-weight:400;font-size:19px;line-height:24px;color:var(--ink);margin:12px 16px 0}
  .post p{font-family:"PT Sans",sans-serif;font-size:13px;line-height:19px;margin:8px 14px 0 16px;color:var(--text)}
  .post .btn{position:absolute;left:16px;bottom:16px}

  /* footer */
  .footer-nav{position:absolute;left:0;top:2358px;width:1200px;height:45px;background:var(--footer-nav);display:flex;justify-content:center;align-items:center;gap:40px;
    font-family:"Poppins",sans-serif;font-size:12px;color:var(--ink)}
  .footer-nav a{color:inherit;text-decoration:none}
  .footer-bar{position:absolute;left:0;top:2403px;width:1200px;height:36px;background:var(--purple);color:var(--white);font-size:12px}
  .footer-bar .copy{position:absolute;left:114px;top:10px}
  .footer-bar .social{left:1000px;top:7px}
</style>
</head>
<body>

<div class="topbar">
  <div class="social" aria-label="Social links"><span></span><span></span><span></span></div>
  <div class="lang"><i></i>English ▾</div>
</div>

<header class="header">
  <div class="brand">
    <div class="mark"></div>
    <div class="name">VELUNA</div>
  </div>
  <nav class="nav">
    <a class="active" href="#">HOME</a><span class="dot"></span>
    <a href="#">ABOUT US</a><span class="dot"></span>
    <a href="#">OUR PRODUCTS</a><span class="dot"></span>
    <a href="#">BLOG</a><span class="dot"></span>
    <a href="#">CONTACT US</a>
  </nav>
</header>

<section class="hero" role="img" aria-label="Three supplement bottles standing on a wooden table in front of a blurred interior">
  <div class="hero-products" role="img" aria-label="Three white supplement bottles: Vitalis Mono, B-Vital and Herba Focus"></div>
  <div class="hero-copy">
    <h1>WELL BEING THROUGH<br>SMART RESEARCH</h1>
    <p>Balance your life &amp; nourish your soul</p>
  </div>
  <a class="btn-hero" href="#">PLACE YOUR ORDER AT BRIXEL</a>
</section>

<section class="about">
  <h2 class="section-title">About <b>VELUNA</b></h2>
  <div class="divider"></div>
  <h3>Lorem Ipsum is simply dummy text of the printing and typesetting industry.</h3>
  <p class="lead">Lorem Ipsum has been the industry's standard dummy text ever since the 1500s, when an unknown printer took a galley of type and scrambled it to make a type specimen book. It has survived not only five centuries, but also the leap into electronic typesetting, remaining essentially unchanged. It was popularised in the 1960s with the release of Typeset sheets containing Lorem Ipsum passages, and more recently with desktop publishing software like Layoutly including versions of Lorem Ipsum.</p>
  <a class="btn" href="#">READ MORE</a>
</section>

<section class="products on-grey">
  <h2 class="section-title">Our <b>PRODUCTS</b></h2>
  <div class="divider"></div>
  <div class="product-grid">
    <article class="product-card">
      <div class="product-image" role="img" aria-label="White supplement bottle with a teal label"></div>
      <h4>SMART<br>MINDPLEX</h4>
      <p>Lorem Ipsum has been the industry's standard dummy text ever since the of Lorem Ipsum.</p>
      <a class="btn" href="#">READ MORE</a>
    </article>
    <article class="product-card">
      <div class="product-image" role="img" aria-label="White supplement bottle with a green label"></div>
      <h4>VITALIS<br>MONO</h4>
      <p>Lorem Ipsum has been the industry's standard dummy text ever since the of Lorem Ipsum.</p>
      <a class="btn" href="#">READ MORE</a>
    </article>
    <article class="product-card">
      <div class="product-image" role="img" aria-label="White supplement bottle with a blue label"></div>
      <h4>B-VITAL</h4>
      <p>Lorem Ipsum has been the industry's standard dummy text ever since the of Lorem Ipsum.</p>
      <a class="btn" href="#">READ MORE</a>
    </article>
    <article class="product-card">
      <div class="product-image" role="img" aria-label="White supplement bottle with a teal label"></div>
      <h4>COSMETIC<br>OIL</h4>
      <p>Lorem Ipsum has been the industry's standard dummy text ever since the of Lorem Ipsum.</p>
      <a class="btn" href="#">READ MORE</a>
    </article>
  </div>
</section>

<section class="blog">
  <h2 class="section-title">Latest <b>BLOG</b></h2>
  <div class="divider"></div>
  <div class="blog-grid">
    <article class="post">
      <div class="post-image beach" role="img" aria-label="Happy couple on a sunny beach"><span class="date">Nov 03, 2017</span></div>
      <div class="meta">
        <span class="author"><svg width="10" height="11" viewBox="0 0 10 11"><circle cx="5" cy="3" r="2.6"/><path d="M0 11c0-3.3 2.2-5 5-5s5 1.7 5 5z"/></svg>Lena Hart</span>
        <span class="stats">
          <span><svg width="12" height="10" viewBox="0 0 12 10"><path d="M1 1h10v6H5l-3 2.5V7H1z"/></svg>111</span>
          <span><svg width="11" height="10" viewBox="0 0 11 10"><path d="M5.5 10 1 5.5A2.8 2.8 0 0 1 5.5 1.5 2.8 2.8 0 0 1 10 5.5z"/></svg>160</span>
        </span>
      </div>
      <h4>Smart Living</h4>
      <p>Text search has become an essential requirement for any modern web application. Often we require advanced search capabilities in our</p>
      <a class="btn" href="#">READ MORE</a>
    </article>
    <article class="post">
      <div class="post-image waist" role="img" aria-label="Person measuring their waist with a tape"><span class="date">Nov 03, 2017</span></div>
      <div class="meta">
        <span class="author"><svg width="10" height="11" viewBox="0 0 10 11"><circle cx="5" cy="3" r="2.6"/><path d="M0 11c0-3.3 2.2-5 5-5s5 1.7 5 5z"/></svg>Lena Hart</span>
        <span class="stats">
          <span><svg width="12" height="10" viewBox="0 0 12 10"><path d="M1 1h10v6H5l-3 2.5V7H1z"/></svg></span>
          <span><svg width="11" height="10" viewBox="0 0 11 10"><path d="M5.5 10 1 5.5A2.8 2.8 0 0 1 5.5 1.5 2.8 2.8 0 0 1 10 5.5z"/></svg>160</span>
        </span>
      </div>
      <h4>Smart Dieting</h4>
      <p>Text search has become an essential requirement for any modern web application. Often we require advanced search capabilities in our</p>
      <a class="btn" href="#">READ MORE</a>
    </article>
    <article class="post">
      <div class="post-image fitness" role="img" aria-label="Two women exercising on fitness balls"><span class="date">Nov 03, 2017</span></div>
      <div class="meta">
        <span class="author"><svg width="10" height="11" viewBox="0 0 10 11"><circle cx="5" cy="3" r="2.6"/><path d="M0 11c0-3.3 2.2-5 5-5s5 1.7 5 5z"/></svg>Lena Hart</span>
        <span class="stats">
          <span><svg width="12" height="10" viewBox="0 0 12 10"><path d="M1 1h10v6H5l-3 2.5V7H1z"/></svg>111</span>
          <span><svg width="11" height="10" viewBox="0 0 11 10"><path d="M5.5 10 1 5.5A2.8 2.8 0 0 1 5.5 1.5 2.8 2.8 0 0 1 10 5.5z"/></svg>160</span>
        </span>
      </div>
      <h4>Smart Body</h4>
      <p>Text search has become an essential requirement for any modern web application. Often we require advanced search capabilities in our</p>
      <a class="btn" href="#">READ MORE</a>
    </article>
  </div>
</section>

<nav class="footer-nav">
  <a href="#">HOME</a><a href="#">ABOUT US</a><a href="#">OUR PRODUCTS</a><a href="#">BLOG</a><a href="#">CONTACT US</a>
</nav>
<footer class="footer-bar">
  <span class="copy">Copyright 2015 Veluna. All rights reserved.</span>
  <div class="social" aria-label="Social links"><span></span><span></span><span></span></div>
</footer>

</body>
</html>
```